Carrow Equity Webinar Ads

Need a banner pack in less than 48 hours for this website:
http://carrowequity-example.com/webinar
Target Market(s)
Accredited real estate investors looking to grow their portfolio
Font styles to use
Sans Serif
Colors
0255a3
f37123
000000

```html
<!DOCTYPE html>
<html lang="en">
<head>
<meta charset="utf-8">
<title>Carrow Equity Webinar Ads</title>
<link href="https://fonts.googleapis.com/css2?family=PT+Sans+Narrow:wght@400;700&family=Open+Sans:wght@400;600;700&display=swap" rel="stylesheet">
<style>
  :root {
    --stage-top: #a9cdd3;
    --stage-bottom: #6fa0ab;
    --banner-white: #ffffff;
    --heading-blue: #2d76a3;
    --panel-blue: #0b5fb8;
    --text-dark: #222222;
    --text-white: #ffffff;
    --button-orange: #f5a400;
    --button-orange-deep: #e58d00;
    --button-tab: #b87400;
    --night: #121212;
    --name-ink: #1d3f5c;
  }
  * { box-sizing: border-box; margin: 0; padding: 0; }
  html, body { width: 1200px; height: 830px; overflow: hidden; }
  body {
    background: radial-gradient(ellipse at 40% 30%, var(--stage-top), var(--stage-bottom));
    font-family: "Open Sans", Arial, sans-serif;
    color: var(--text-dark);
  }
  .stage {
    position: relative;
    width: 1103px; height: 763px;
    transform: scale(1.0879);
    transform-origin: 0 0;
  }
  .banner {
    position: absolute;
    overflow: hidden;
    background: var(--banner-white);
    box-shadow: 0 1px 4px rgba(0,0,0,.15);
  }
  .headline {
    font-family: "PT Sans Narrow", "Arial Narrow", sans-serif;
    font-weight: 700;
    color: var(--heading-blue);
    line-height: 1.05;
    white-space: nowrap;
  }
  .body-copy { font-size: 12px; line-height: 1.5; text-align: center; white-space: nowrap; }
  .body-copy b { font-weight: 700; }
  .brand {
    position: absolute;
    display: flex; align-items: center; gap: 6px;
    font-family: "Open Sans", Arial, sans-serif;
    font-weight: 600;
    color: var(--name-ink);
    white-space: nowrap;
  }
  .brand .dot { width: 10px; height: 10px; border-radius: 50%; background: var(--heading-blue); }
  .brand.light { color: var(--text-white); }
  .brand.light .dot { background: var(--text-white); }
  .cta {
    position: absolute;
    display: flex; align-items: stretch;
    background: linear-gradient(var(--button-orange), var(--button-orange-deep));
    color: var(--text-white);
    font-family: "PT Sans Narrow", "Arial Narrow", sans-serif;
    white-space: nowrap;
  }
  .cta span { flex: 1; display: flex; align-items: center; justify-content: center; }
  .cta .tab { flex: 0 0 auto; display: flex; align-items: center; justify-content: center; background: var(--button-tab); }
  .photo { position: absolute; }
  .url {
    position: absolute; left: 0; right: 0; bottom: 0;
    background: var(--banner-white);
    font-size: 6.5px; font-weight: 600; text-align: center; line-height: 11px; white-space: nowrap;
  }

  /* skyscraper A */
  .sky-a { left: 121px; top: 73px; width: 141px; height: 527px; background: var(--night); }
  .sky-a .photo-top { left: 0; top: 0; width: 141px; height: 97px; background: linear-gradient(135deg, #8a6a3a, #5b4327 60%, #3a2c1e); }
  .sky-a .blue-panel { position: absolute; left: 0; top: 99px; width: 141px; height: 196px; background: var(--panel-blue); color: var(--text-white); text-align: center; }
  .sky-a .blue-panel .headline { color: var(--text-white); font-size: 19px; margin-top: 8px; }
  .sky-a .blue-panel .body-copy { margin-top: 12px; font-size: 11.5px; line-height: 1.6; }
  .sky-a .dark-panel { position: absolute; left: 0; top: 298px; width: 141px; height: 218px; background: linear-gradient(#2a2a2a, #111 45%, #1a1a1a); text-align: center; color: var(--text-white); }
  .sky-a .dark-panel .headline { color: var(--text-white); font-size: 19px; margin-top: 30px; }
  .sky-a .dark-panel ul { list-style: none; margin-top: 16px; font-family: "PT Sans Narrow", sans-serif; font-size: 14px; line-height: 1.3; white-space: nowrap; }
  .sky-a .dark-panel ul li:first-child { font-size: 15px; }

  /* skyscraper B */
  .sky-b { left: 276px; top: 73px; width: 141px; height: 527px; }
  .sky-b .headline { position: absolute; left: 0; right: 0; top: 122px; text-align: center; font-size: 19px; }
  .sky-b .body-copy { position: absolute; left: 0; right: 0; top: 204px; font-size: 10.5px; line-height: 1.55; letter-spacing: -0.1px; }
  .sky-b .photo { left: 0; top: 330px; width: 141px; height: 150px; background: linear-gradient(160deg, #9a6a3e, #6a4328 55%, #2e2118); clip-path: polygon(0 0, 100% 22%, 100% 100%, 0 100%); }

  /* medium rectangles */
  .rect-c { left: 426px; top: 73px; width: 300px; height: 250px; }
  .rect-c .headline { position: absolute; left: 0; right: 0; top: 93px; text-align: center; font-size: 21px; }
  .rect-c .body-copy { position: absolute; left: 0; right: 0; top: 130px; font-size: 12.5px; line-height: 1.45; }

  .rect-d { left: 426px; top: 337px; width: 300px; height: 250px; }
  .rect-d .photo { right: 0; top: 0; width: 130px; height: 250px; background: linear-gradient(200deg, #5a7aa0, #3a3f50 40%, #6a4a34 75%, #2a2622); clip-path: polygon(68% 0, 100% 0, 100% 100%, 0 100%); }
  .rect-d .headline { position: absolute; left: 14px; top: 82px; font-size: 16.5px; }
  .rect-d .body-copy { position: absolute; left: 14px; top: 114px; text-align: left; font-size: 12px; line-height: 1.5; }

  .rect-e { left: 738px; top: 337px; width: 300px; height: 250px; background: linear-gradient(160deg, #4a3a30, #2a2420 45%, #3a2e26 75%, #1a1614); }
  .rect-e .headline { position: absolute; left: 0; right: 0; top: 86px; text-align: center; font-size: 18.5px; color: var(--text-white); }
  .rect-e .body-copy { position: absolute; left: 0; right: 0; top: 121px; color: var(--text-white); font-family: "PT Sans Narrow", sans-serif; font-size: 15.5px; line-height: 1.4; }

  /* leaderboard */
  .leader { left: 121px; top: 612px; width: 728px; height: 90px; }
  .leader .headline { position: absolute; left: 15px; top: 20px; font-size: 24px; }
  .leader .body-copy { position: absolute; left: 228px; width: 276px; top: 17px; font-size: 12.5px; line-height: 1.45; }
</style>
</head>
<body>
<div class="stage">

  <section class="banner sky-a">
    <div class="photo photo-top" role="img" aria-label="Blurred warm-toned photo behind the brand name"></div>
    <div class="brand light" style="left:12px; top:40px; font-size:11.5px;"><i class="dot"></i>Carrow Equity</div>
    <div class="blue-panel">
      <h2 class="headline">Simple 6 Step<br>Blueprint<br>Reveals...</h2>
      <p class="body-copy">How Over 800 Real<br>Estate Investors<br><b>Earned</b> An Average<br>Of Over <b>$30,000</b><br>Each In Passive Rental<br>Income In 2014!</p>
    </div>
    <div class="dark-panel">
      <h3 class="headline">All Without</h3>
      <ul>
        <li>Buying A Course</li>
        <li>Attending A Seminar</li>
        <li>Investing In Coaching</li>
      </ul>
      <svg width="40" height="36" viewBox="0 0 40 36" style="margin-top:10px;" aria-hidden="true">
        <g fill="none" stroke="#d0d0d0" stroke-width="2">
          <path d="M14 2v30M8 24l6 8 6-8"/>
          <path d="M26 2v30M20 24l6 8 6-8"/>
        </g>
      </svg>
      <a class="cta" style="left:19px; top:191px; width:103px; height:21px; font-size:13px;"><span>Register Now</span><i class="tab" style="width:14px;"><svg width="8" height="8" viewBox="0 0 8 8"><path d="M1 1l3 3-3 3M4 1l3 3-3 3" fill="none" stroke="#fff" stroke-width="1.3"/></svg></i></a>
    </div>
    <p class="url">http://carrowequity-example.com/webinar</p>
  </section>

  <section class="banner sky-b">
    <div class="brand" style="left:14px; top:45px; font-size:12px;"><i class="dot"></i>Carrow Equity</div>
    <h2 class="headline">Simple 6 Step<br>Blueprint Reveals</h2>
    <p class="body-copy">How Over <b>800 Real</b><br><b>Estate Investors</b> Earned<br>An Average Of Over<br><b>$30,000</b> Each In <b>Passive</b><br><b>Rental Income</b> In 2014...</p>
    <div class="photo" role="img" aria-label="Photo of a seminar audience seated in rows"></div>
    <a class="cta" style="left:19px; top:487px; width:103px; height:21px; font-size:13px;"><span>Register Now</span><i class="tab" style="width:14px;"><svg width="8" height="8" viewBox="0 0 8 8"><path d="M1 1l3 3-3 3M4 1l3 3-3 3" fill="none" stroke="#fff" stroke-width="1.3"/></svg></i></a>
    <p class="url">http://carrowequity-example.com/webinar</p>
  </section>

  <section class="banner rect-c">
    <div class="brand" style="left:75px; top:40px; font-size:18px;"><i class="dot"></i>Carrow Equity</div>
    <h2 class="headline">Simple 6 Step Blueprint Reveals...</h2>
    <p class="body-copy">How Over <b>800 Real Estate Investors</b><br>Earned An Average Of Over <b>$30,000</b><br>Each In <b>Passive Rental Income</b> In 2014...</p>
    <a class="cta" style="left:46px; top:205px; width:211px; height:29px; font-size:16px;"><span>Register For The Webinar</span><i class="tab" style="width:30px;"><svg width="12" height="11" viewBox="0 0 12 11"><path d="M1 1l4 4.5-4 4.5M6 1l4 4.5-4 4.5" fill="none" stroke="#fff" stroke-width="1.8"/></svg></i></a>
  </section>

  <section class="banner rect-d">
    <div class="photo" role="img" aria-label="Photo of a seminar audience facing a screen"></div>
    <div class="brand" style="left:14px; top:45px; font-size:16px;"><i class="dot"></i>Carrow Equity</div>
    <h2 class="headline">Simple 6 Step Blueprint Reveals...</h2>
    <p class="body-copy">How Over <b>800 Real Estate</b><br><b>Investors</b> Earned An Average<br>Of Over <b>$30,000</b> Each In<br><b>Passive Rental Income</b><br>In 2014...</p>
    <a class="cta" style="left:14px; top:212px; width:211px; height:29px; font-size:16px;"><span>Register For The Webinar</span><i class="tab" style="width:30px;"><svg width="12" height="11" viewBox="0 0 12 11"><path d="M1 1l4 4.5-4 4.5M6 1l4 4.5-4 4.5" fill="none" stroke="#fff" stroke-width="1.8"/></svg></i></a>
  </section>

  <section class="banner rect-e" role="img" aria-label="Dark blurred photo of a seminar audience">
    <div class="brand light" style="left:97px; top:32px; font-size:14px;"><i class="dot"></i>Carrow Equity</div>
    <h2 class="headline">Simple 6 Step Blueprint Reveals...</h2>
    <p class="body-copy">How Over 800 Real Estate Investors<br>Earned An Average Of Over $30,000<br>Each In Passive Rental Income In 2014</p>
    <svg style="position:absolute; left:20px; top:196px;" width="42" height="44" viewBox="0 0 42 44" aria-hidden="true">
      <g fill="none" stroke="#fff" stroke-width="2" stroke-linecap="round">
        <path d="M12 2C4 14 6 30 34 36"/>
        <path d="M26 29l8 7-9 5"/>
      </g>
    </svg>
    <a class="cta" style="left:63px; top:209px; width:211px; height:29px; font-size:16px;"><span>Register For The Webinar</span><i class="tab" style="width:30px;"><svg width="12" height="11" viewBox="0 0 12 11"><path d="M1 1l4 4.5-4 4.5M6 1l4 4.5-4 4.5" fill="none" stroke="#fff" stroke-width="1.8"/></svg></i></a>
  </section>

  <section class="banner leader">
    <h2 class="headline">Simple 6 Step<br>Blueprint Reveals...</h2>
    <p class="body-copy">How Over <b>800 Real Estate Investors</b><br>Earned An Average Of Over <b>$30,000</b><br>Each In <b>Passive Rental Income</b> In 2014...</p>
    <div class="brand" style="left:580px; top:27px; font-size:13px;"><i class="dot"></i>Carrow Equity</div>
    <a class="cta" style="left:546px; top:59px; width:174px; height:25px; font-size:14px;"><span>Register For The Webinar</span><i class="tab" style="width:22px;"><svg width="10" height="10" viewBox="0 0 10 10"><path d="M1 1l3.5 4-3.5 4M5 1l3.5 4-3.5 4" fill="none" stroke="#fff" stroke-width="1.6"/></svg></i></a>
  </section>

</div>
</body>
</html>
```